Cover needed for book, Wedded to the Fellow Who Drifted Out to Sea

Cover should use the attached photograph, with the groom faded in some way, to represent the concept in the title. Overall look should tell readers the book is in the genre of Marian's Embers, Never Send Us Back Home etc. Book is memoir of Edith, who was married to a man who had obsessive-compulsive disorder when little was known about the condition.

Text should be

Wedded to the Fellow Who Drifted Out to Sea
The true story of how obsession tore a family apart
By Edith Harcombe

```html
<!DOCTYPE html>
<html lang="en">
<head>
<meta charset="utf-8">
<title>Wedded to the Fellow Who Drifted Out to Sea — Book Cover</title>
<link rel="stylesheet" href="https://fonts.googleapis.com/css2?family=Righteous&family=Abril+Fatface&display=swap">
<style>
  :root {
    --sky-light: #d6eaf2;
    --sky-mid: #82b8d0;
    --sky-deep: #4f8fae;
    --ink: #231f20;
    --slate: rgba(34, 46, 60, 0.86);
    --photo-light: #e2e2df;
    --photo-mid: #a9abaa;
    --photo-dark: #3f4a55;
    --groom-fade: #6f8ea3;
    --band: #262626;
    --accent: #3aa3c6;
  }
  * { margin: 0; padding: 0; box-sizing: border-box; }
  html, body { width: 1200px; height: 818px; overflow: hidden; background: #ffffff; }
  .cover {
    position: relative;
    width: 1200px;
    height: 818px;
    overflow: hidden;
    background:
      radial-gradient(ellipse at 20% 12%, var(--sky-light) 0%, transparent 40%),
      radial-gradient(ellipse at 52% 80%, #eaf4f8 0%, transparent 30%),
      radial-gradient(ellipse at 60% 30%, var(--sky-mid) 0%, transparent 55%),
      linear-gradient(160deg, var(--sky-mid) 0%, var(--sky-deep) 55%, #8cc0d6 100%);
    font-family: 'Righteous', sans-serif;
    color: var(--ink);
  }

  /* back cover photograph */
  .back-photo {
    position: absolute;
    left: 155px; top: 302px;
    width: 250px; height: 505px;
    border-radius: 48% 48% 14% 14% / 30% 30% 8% 8%;
    background:
      linear-gradient(90deg, rgba(79,143,174,0) 0%, var(--photo-dark) 18%, var(--photo-dark) 45%, var(--photo-mid) 55%, var(--photo-light) 75%, rgba(217,217,214,0) 100%);
    -webkit-mask-image: radial-gradient(ellipse 55% 60% at 50% 50%, #000 60%, transparent 100%);
            mask-image: radial-gradient(ellipse 55% 60% at 50% 50%, #000 60%, transparent 100%);
  }

  /* front cover photograph */
  .front-photo {
    position: absolute;
    left: 660px; top: 0;
    width: 540px; height: 818px;
    -webkit-mask-image: linear-gradient(90deg, transparent 0%, #000 22%);
            mask-image: linear-gradient(90deg, transparent 0%, #000 22%);
  }
  .front-photo .photo-groom {
    position: absolute; left: 0; top: 0; width: 270px; height: 818px;
    background: linear-gradient(180deg, #8ea3b1 0%, var(--groom-fade) 40%, #9fb9c8 75%, #d9e9f0 100%);
    opacity: 0.9;
  }
  .front-photo .photo-bride {
    position: absolute; left: 250px; top: 0; width: 290px; height: 818px;
    background:
      radial-gradient(ellipse 60% 30% at 55% 22%, #f0f0ee 0%, transparent 100%),
      linear-gradient(180deg, #8d8f8f 0%, var(--photo-light) 35%, #c4c6c4 60%, var(--photo-light) 100%);
    -webkit-mask-image: linear-gradient(90deg, transparent 0%, #000 12%);
            mask-image: linear-gradient(90deg, transparent 0%, #000 12%);
  }

  .tagline {
    position: absolute;
    left: 85px; top: 96px;
    font-weight: 400;
  }
  .tagline span { display: block; white-space: nowrap; line-height: 1; }
  .tagline .line-1 { font-size: 58px; letter-spacing: 1px; }
  .tagline .line-2 { font-size: 46px; margin-top: 8px; letter-spacing: 0.5px; }
  .tagline .line-2 small { font-size: 24px; }
  .tagline .line-3 { font-size: 60px; margin-top: 8px; letter-spacing: 0.5px; }

  .back-author {
    position: absolute;
    left: 172px; top: 616px;
    font-size: 34px;
    white-space: nowrap;
  }
  .back-author small { font-size: 27px; }
  .isbn {
    position: absolute;
    left: 320px; top: 703px;
    font-family: Arial, Helvetica, sans-serif;
    font-size: 12.5px;
    word-spacing: 8px;
  }
  .spine-title {
    position: absolute;
    left: 589px; top: 70px;
    writing-mode: vertical-rl;
    font-size: 21px;
    white-space: nowrap;
    letter-spacing: 0.3px;
  }
  .front-author {
    position: absolute;
    left: 803px; top: 66px;
    font-size: 30px;
    white-space: nowrap;
  }
  .front-author small { font-size: 24px; }

  .front-title {
    position: absolute;
    left: 682px; top: 122px;
    font-family: 'Abril Fatface', serif;
    font-weight: 400;
    color: var(--slate);
    text-shadow: 1px 1px 0 rgba(255,255,255,0.4);
  }
  .front-title span { display: block; line-height: 0.92; white-space: nowrap; transform-origin: left; transform: scaleX(0.74); }
  .front-title .big { font-size: 100px; }
  .front-title .mid { font-size: 86px; }
  .front-title .small { font-size: 58px; }
  .front-title .last { font-size: 110px; }

  .true-band { position: absolute; left: 0; top: 0; width: 1200px; height: 818px; }
</style>
</head>
<body>
<main class="cover">
  <div class="back-photo" role="img" aria-label="Black and white wedding photograph of the bride and groom, vignetted into the blue wash"></div>
  <div class="front-photo" role="img" aria-label="Enlarged black and white wedding photograph: the groom on the left fades into the blue wash, the bride with her bouquet on the right">
    <div class="photo-groom"></div>
    <div class="photo-bride"></div>
  </div>

  <h2 class="tagline">
    <span class="line-1">The true story</span>
    <span class="line-2"><small>of how</small> obsession tore</span>
    <span class="line-3">a family apart</span>
  </h2>
  <p class="back-author"><small>by</small> Edith Harcombe</p>
  <p class="isbn">ISBN 0-000-0000-0 $0.00</p>

  <p class="spine-title">Wedded to the Fellow Who Drifted Out to Sea&nbsp;&nbsp;by Edith Harcombe</p>

  <p class="front-author"><small>by</small> Edith Harcombe</p>
  <h1 class="front-title">
    <span class="big">Wedded</span>
    <span class="mid">to the</span>
    <span class="big">Fellow</span>
    <span class="small">who</span>
    <span class="big">Drifted</span>
    <span class="mid">Out to</span>
    <span class="last">Sea</span>
  </h1>

  <svg class="true-band" viewBox="0 0 1200 818">
    <polygon points="795,818 868,818 1200,568 1200,508" fill="var(--band)"/>
    <text transform="translate(935,785) rotate(-37)" font-family="Righteous, sans-serif" font-size="46" fill="var(--accent)" letter-spacing="1">TRUE STORY</text>
  </svg>
</main>
</body>
</html>
```